Harbor Business Cards

I need a business card designed with the following information.

Company Name: Harbor Wealth Management
Name: BriAnne Dockery
Title: Executive Assistant
Cell: (555) 555-0173
Direct Line: (555) 555-0148
Email: brianne@harborwmx.com
Address: 20537 W. Marlowe PKWY Ste. B
Westbrook, CO 80390

I have attached the logo.
I would like it in navy blue and silver.
Thanks.

```html
<!DOCTYPE html>
<html lang="en">
<head>
<meta charset="utf-8">
<title>Harbor Wealth Management – Business Card</title>
<link rel="stylesheet" href="https://fonts.googleapis.com/css2?family=Tenor+Sans&display=swap">
<style>
  :root {
    --navy: #232a40;
    --silver: #eceded;
    --paper: #ffffff;
    --backdrop: #dcdcdc;
    --ink: #2b3048;
  }
  * { margin: 0; padding: 0; box-sizing: border-box; }
  html, body {
    width: 1200px; height: 726px; overflow: hidden;
    background: var(--backdrop);
    font-family: "Tenor Sans", sans-serif;
    color: var(--ink);
  }
  .canvas { position: relative; width: 1200px; height: 726px; }
  .card {
    position: absolute; width: 540px; height: 309px;
    background: var(--paper); overflow: hidden;
  }
  .card--front { left: 40px; top: 110px; }
  .card--back { left: 620px; top: 300px; background: var(--silver); }

  .front-mark {
    position: absolute; left: 0; right: 0; top: 92px;
    display: flex; flex-direction: column; align-items: center;
  }
  .brand-square { width: 30px; height: 30px; background: var(--navy); margin-bottom: 16px; }
  .wordmark {
    font-size: 30px; letter-spacing: 16px; padding-left: 16px;
    color: var(--navy); line-height: 1;
  }
  .wordmark-sub {
    font-size: 10.5px; letter-spacing: 5px; padding-left: 5px;
    color: var(--navy); margin-top: 8px;
  }

  .back-decor {
    position: absolute; right: 0; top: 0;
    width: 190px; height: 230px; background: var(--navy);
  }
  .edge-curve {
    position: absolute; left: -18px; top: 190px;
    width: 36px; height: 60px; border-radius: 50%; background: var(--navy);
  }
  .back-brand { position: absolute; left: 34px; top: 92px; }
  .back-brand .wordmark { font-size: 25px; letter-spacing: 12px; padding-left: 0; }
  .back-brand .wordmark-sub { font-size: 9px; letter-spacing: 3.5px; padding-left: 0; margin-top: 6px; }

  .person { position: absolute; left: 34px; top: 162px; }
  .person-name { font-size: 17px; letter-spacing: 0.5px; color: var(--navy); }
  .person-title { font-size: 10.5px; margin-top: 2px; }

  .contact-list { position: absolute; left: 34px; top: 208px; list-style: none; font-size: 11.5px; }
  .contact-list li { display: flex; align-items: center; gap: 9px; height: 15px; }
  .contact-list svg { width: 10px; height: 10px; fill: var(--navy); flex: none; }
  .address { position: absolute; left: 34px; top: 274px; font-size: 11.5px; white-space: nowrap; }
</style>
</head>
<body>
<div class="canvas">

  <section class="card card--front">
    <div class="front-mark">
      <div class="brand-square"></div>
      <div class="wordmark">HARBOR</div>
      <div class="wordmark-sub">WEALTH MANAGEMENT</div>
    </div>
  </section>

  <section class="card card--back">
    <div class="back-decor"></div>
    <div class="edge-curve"></div>

    <div class="back-brand">
      <div class="wordmark">HARBOR</div>
      <div class="wordmark-sub">WEALTH MANAGEMENT</div>
    </div>

    <div class="person">
      <div class="person-name">BRIANNE DOCKERY</div>
      <div class="person-title">Executive Assistant</div>
    </div>

    <ul class="contact-list">
      <li>
        <svg viewBox="0 0 10 10" aria-hidden="true"><rect x="2.5" y="0" width="5" height="10" rx="1"/><rect x="3.5" y="1.5" width="3" height="5.5" fill="#eceded"/></svg>
        (555) 555-0173
      </li>
      <li>
        <svg viewBox="0 0 10 10" aria-hidden="true"><path d="M0 3 Q5 0 10 3 L9 5 L7 4 L7 3 Q5 2 3 3 L3 4 L1 5 Z"/><rect x="2" y="5" width="6" height="4" rx="0.5"/></svg>
        (555) 555-0148
      </li>
      <li>
        <svg viewBox="0 0 10 10" aria-hidden="true"><rect x="0" y="2" width="10" height="6.5"/><path d="M0.5 2.5 L5 6 L9.5 2.5" fill="none" stroke="#eceded" stroke-width="0.9"/></svg>
        brianne@harborwmx.com
      </li>
      <li>
        <svg viewBox="0 0 10 10" aria-hidden="true"><circle cx="5" cy="5" r="4.5"/><path d="M0.5 5 H9.5 M5 0.5 V9.5" stroke="#eceded" stroke-width="0.7"/></svg>
        www.harborwmx.com
      </li>
    </ul>

    <div class="address">20537 W. Marlowe PKWY Ste. B Westbrook, CO 80390</div>
  </section>

</div>
</body>
</html>
```